Business card design needed

Chasing a very simplistic modern design with a logo incorporating "RTK".
I'm starting a plumbing business.
I do water, sanitary and drainage plumbing that will cover residential, commercial, rental, rural, excavation, new housing and all maintanence requirements.

Industry/Entity Type

Business

Contact Information for Business Card

RTK PLUMBING SERVICES
DAVID TRELOWEN - LICENSED PLUMBER
PHONE: 0481956274
E-MAIL: trelodw7@kestrelnet.com
NORTHERN SUBURBS

Requirements
Must have
• lower case email address

```html
<!DOCTYPE html>
<html lang="en">
<head>
<meta charset="utf-8">
<title>RTK Plumbing Services – Business Card</title>
<link rel="stylesheet" href="https://fonts.googleapis.com/css2?family=Open+Sans:wght@400;600;700;800&display=swap">
<style>
  :root {
    --stage-blue: #1072bb;
    --card-black: #000000;
    --card-white: #ffffff;
    --brand-blue: #1e8fd5;
    --name-blue: #1878c0;
    --text-grey: #858585;
    --silver: #b4b6b8;
    --dark-steel: #2a2a2a;
  }
  * { margin: 0; padding: 0; box-sizing: border-box; }
  html, body {
    width: 1200px; height: 900px; overflow: hidden;
    background: var(--stage-blue);
    font-family: "Open Sans", Arial, sans-serif;
  }
  .canvas { position: relative; width: 1200px; height: 900px; }

  .card { position: absolute; left: 256px; width: 689px; overflow: hidden; }
  .card--front { top: 18px; height: 422px; background: var(--card-white); }
  .card--back { top: 459px; height: 421px; background: var(--card-black); }

  .front-header { position: absolute; left: 0; top: 0; width: 100%; height: 216px; background: var(--card-black); }
  .header-rule { position: absolute; left: 0; top: 204px; width: 100%; height: 9px; background: var(--card-black); }
  .steel-band {
    position: absolute; left: 0; width: 100%;
    background: linear-gradient(90deg, var(--card-black) 0%, var(--dark-steel) 15%, var(--silver) 50%, var(--dark-steel) 85%, var(--card-black) 100%);
  }
  .steel-band--top { top: 204px; height: 9px; }
  .steel-band--bottom { top: 394px; height: 28px; }
  .divider-black { position: absolute; left: 0; top: 198px; width: 100%; height: 3px; background: var(--card-white); }

  .brand-name {
    position: absolute; left: 42px; top: 22px;
    font-size: 104px; font-weight: 800; line-height: 1; letter-spacing: 2px;
    color: var(--brand-blue);
  }
  .brand-tagline {
    position: absolute; left: 42px; top: 126px;
    font-size: 32px; font-weight: 700; letter-spacing: 1.5px;
    color: var(--card-white); line-height: 1;
  }
  .service-list {
    position: absolute; left: 484px; top: 60px; list-style: none;
    color: var(--card-white); font-size: 21px; line-height: 38px; letter-spacing: 0.5px;
  }

  .person { position: absolute; left: 50px; top: 268px; }
  .person-name { font-size: 24px; font-weight: 700; color: var(--name-blue); line-height: 32px; }
  .person-role { font-size: 21px; color: var(--text-grey); line-height: 30px; }

  .contact { position: absolute; left: 416px; top: 297px; list-style: none; color: var(--text-grey); font-size: 19px; }
  .contact li { display: flex; align-items: center; height: 30px; }
  .contact-icon { width: 26px; height: 20px; margin-right: 7px; fill: var(--name-blue); }
  .contact-area { margin-top: 1px; }

  .back-brand {
    position: absolute; left: 0; width: 100%; top: 150px; text-align: center;
    font-size: 90px; font-weight: 800; line-height: 1; letter-spacing: 2px;
    color: var(--brand-blue);
  }
  .back-rule {
    position: absolute; left: 172px; top: 253px; width: 342px; height: 4px;
    background: linear-gradient(90deg, transparent 0%, var(--dark-steel) 15%, #e8e8e8 50%, var(--dark-steel) 85%, transparent 100%);
  }
</style>
</head>
<body>
<main class="canvas">
  <section class="card card--front">
    <div class="front-header">
      <div class="brand-name">RTK</div>
      <div class="brand-tagline">Plumbing Services</div>
      <ul class="service-list">
        <li>Residential</li>
        <li>Commercial</li>
        <li>Maintanence</li>
      </ul>
    </div>
    <div class="divider-black" style="top:201px;height:3px;background:var(--card-white)"></div>
    <div class="steel-band steel-band--top"></div>

    <div class="person">
      <div class="person-name">DAVID TRELOWEN</div>
      <div class="person-role">Licenced Plumber</div>
    </div>

    <ul class="contact">
      <li>
        <svg class="contact-icon" viewBox="0 0 26 20" aria-hidden="true">
          <path d="M1 7 C4 1 22 1 25 7 L25 9 L19 9 L18 6 C14 5 12 5 8 6 L7 9 L1 9 Z"/>
          <path d="M7 10 L9 7 L17 7 L19 10 L22 18 L4 18 Z"/>
        </svg>
        0481956274
      </li>
      <li>
        <svg class="contact-icon" viewBox="0 0 26 20" aria-hidden="true">
          <path d="M2 2 H24 V18 H2 Z M4.5 4 L13 11 L21.5 4 Z M4 5.5 V16 H22 V5.5 L13 13 Z M4 16 L10 10.5 L11 11.3 L5.5 16 Z M22 16 L16 10.5 L15 11.3 L20.5 16 Z" fill-rule="evenodd"/>
        </svg>
        trelodw7@kestrelnet.com
      </li>
      <li class="contact-area">Northern Suburbs</li>
    </ul>

    <div class="steel-band steel-band--bottom"></div>
  </section>

  <section class="card card--back">
    <div class="back-brand">RTK</div>
    <div class="back-rule"></div>
  </section>
</main>
</body>
</html>
```